NEW Business Cards!
CNC Machine Shop Business Cards
Simple
Dale Workman
248 North Route 371
Kelvale, Texas 75418
WorkmanIronCraft@mailbox-example.com
www.WorkmanIronCraft.example
We also need this person on the same card somehow:
Travis Workman
Cell - 555.218.7730
Fax - Same
email - Same
In-House Services:
CNC Milling
CNC Turning
CNC Bending
Water Jet Cutting
Powder Coating

```html
<!DOCTYPE html>
<html lang="en">
<head>
<meta charset="utf-8">
<title>Workman Metal Works – Business Cards</title>
<link href="https://fonts.googleapis.com/css2?family=Exo+2:wght@700&family=Arimo:wght@400;700&display=swap" rel="stylesheet">
<style>
  :root {
    --backdrop: #e9e7e4;
    --card: #ffffff;
    --navy: #1c3f7c;
    --blue: #2466c4;
    --gold: #b8924f;
    --gold-dark: #7d6134;
    --ink: #3a3a3a;
    --rule: #9aa3b1;
  }
  * { margin: 0; padding: 0; box-sizing: border-box; }
  html, body { width: 1200px; height: 696px; overflow: hidden; }
  body { background: var(--backdrop); position: relative; font-family: "Arimo", Arial, sans-serif; }

  .card {
    position: absolute;
    top: 245px;
    width: 384px;
    height: 216px;
    background: var(--card);
    border-radius: 10px;
    overflow: hidden;
    box-shadow: 0 4px 12px rgba(0,0,0,.18);
  }
  .card--front { left: 187px; }
  .card--back { left: 600px; }

  .brand-square { position: absolute; background: var(--blue); }
  .brand-name {
    position: absolute;
    font-family: "Exo 2", Arial, sans-serif;
    font-weight: 700;
    color: var(--navy);
    line-height: 1;
  }

  .card--front .brand-square { left: 70px; top: 24px; width: 54px; height: 54px; }
  .card--front .brand-name { left: 138px; top: 32px; font-size: 27px; letter-spacing: 0.5px; }
  .card--front .brand-name small { display: block; font-size: 10px; letter-spacing: 3.2px; margin-top: 3px; }

  .people { position: absolute; left: 50px; top: 110px; width: 120px; }
  .holder-name { font-size: 14px; font-weight: 700; color: var(--blue); line-height: 17px; }
  .holder-name--second { font-size: 11px; line-height: 14px; margin-top: 8px; }
  .holder-cell { font-size: 6.5px; line-height: 9px; color: var(--ink); }

  .address, .contacts {
    position: absolute; left: 178px;
    font-size: 6.5px; line-height: 9px; color: var(--ink);
  }
  .address { top: 113px; }
  .contacts { top: 138px; }
  .contacts span { display: inline-block; width: 24px; }

  .swoosh { position: absolute; left: 0; top: 0; }

  .card--back .brand-square { left: 73px; top: 70px; width: 36px; height: 36px; }
  .card--back .brand-name { left: 48px; top: 114px; font-size: 16px; width: 86px; text-align: center; }
  .divider { position: absolute; left: 199px; top: 38px; width: 1px; height: 160px; background: var(--rule); }
  .services { position: absolute; left: 211px; top: 62px; color: var(--navy); }
  .services h2 { font-size: 13px; font-weight: 700; margin-bottom: 5px; }
  .services ul { list-style: none; font-size: 12px; line-height: 19px; color: var(--ink); }
  .services li::before { content: "- "; }
  .web-line {
    position: absolute; left: 0; right: 0; top: 199px;
    text-align: center; font-size: 6.5px; color: var(--ink);
  }
</style>
</head>
<body>
  <section class="card card--front" aria-label="Card front">
    <svg class="swoosh" width="384" height="216" viewBox="0 0 384 216" aria-hidden="true">
      <path d="M90,216 C200,202 300,194 384,184 L384,216 Z" fill="var(--gold)"/>
      <path d="M150,216 C240,208 320,202 384,198 L384,216 Z" fill="var(--gold-dark)" opacity=".55"/>
      <path d="M0,176 C120,200 260,196 384,176 L384,184 C260,204 120,208 0,190 Z" fill="var(--blue)"/>
      <path d="M0,192 C120,210 250,208 384,190" fill="none" stroke="var(--navy)" stroke-width="1.2"/>
    </svg>
    <div class="brand-square"></div>
    <div class="brand-name">WORKMAN<small>METAL WORKS</small></div>
    <div class="people">
      <div class="holder-name">Dale Workman</div>
      <div class="holder-name holder-name--second">Travis Workman</div>
      <div class="holder-cell">Cell: 555.218.7730</div>
    </div>
    <div class="address">248 North Route 371<br>Kelvale, Texas 75418</div>
    <div class="contacts">
      <span>Cell:</span>555.304.6129<br>
      <span>Fax:</span>555.471.0286<br>
      <span>Email:</span>WorkmanIronCraft@mailbox-example.com<br>
      <span>Web:</span>www.WorkmanIronCraft.example
    </div>
  </section>

  <section class="card card--back" aria-label="Card back">
    <div class="brand-square"></div>
    <div class="brand-name">WORKMAN</div>
    <div class="divider"></div>
    <div class="services">
      <h2>In-House Services:</h2>
      <ul>
        <li>CNC Milling</li>
        <li>CNC Turning</li>
        <li>CNC Bending</li>
        <li>Water Jet Cutting</li>
        <li>Powder Coating</li>
      </ul>
    </div>
    <div class="web-line">www.WorkmanIronCraft.example</div>
  </section>
</body>
</html>
```